Presentation Folder, Business Card, Letterhead and Envelope design

We are a dental clinic that will open in August and we are looking for a professional graphic designer to create our Business Card, Presentation Folder, Letterhead, Notepad and envelopes.

The brand LumaGrin must reflect a sense of quality and sophistication, marketed for middle-class consumers.
Our preference is for quality and refined materials, where less is more.
Attached the logo

```html
<!DOCTYPE html>
<html lang="en">
<head>
<meta charset="utf-8">
<title>LumaGrin Stationery Set</title>
<link rel="stylesheet" href="https://fonts.googleapis.com/css2?family=Montserrat:wght@300;400;600&display=swap">
<style>
:root{
  --bg:#ebebeb;
  --paper:#f3f3f3;
  --paper-edge:#dcdcdc;
  --red:#6f1f22;
  --red-deep:#6a0f10;
  --grey:#6b6b6b;
  --grey-light:#9a9a9a;
  --ink:#3c3c3c;
  --rule:#c9c9c9;
}
*{box-sizing:border-box;margin:0;padding:0}
html,body{width:1200px;height:1057px;overflow:hidden;background:var(--bg);font-family:"Montserrat",sans-serif;color:var(--ink)}
.canvas{position:relative;width:1200px;height:1057px}
.piece{position:absolute;background:var(--paper);box-shadow:0 1px 3px rgba(0,0,0,.12)}

/* brand name lockup */
.brand{display:flex;align-items:center;font-weight:300;text-transform:uppercase;letter-spacing:.2em;color:var(--grey);white-space:nowrap;line-height:1}
.brand .mark{display:block;background:var(--red);flex:none}
.brand--light{color:#fff}
.brand--light .mark{background:#fff}

/* edge band: red then grey */
.edge-band{position:absolute;left:0;right:0;bottom:0;height:3px;background:linear-gradient(100deg,var(--red) 0 74%,var(--grey-light) 74% 100%)}

/* banner */
.banner{left:50px;top:42px;width:1118px;height:111px;border-radius:4px}
.banner .brand{position:absolute;left:390px;top:30px;font-size:50px;letter-spacing:.17em}
.banner .mark{width:52px;height:52px;margin-right:14px}

/* notepad */
.notepad{left:92px;top:195px;width:185px;height:265px}
.notepad .rings{position:absolute;top:-6px;left:8px;right:8px;display:flex;justify-content:space-between}
.notepad .rings span{width:4px;height:14px;border:1.5px solid #a8a8a8;border-radius:3px}
.notepad .brand{position:absolute;left:14px;top:32px;font-size:7.5px}
.notepad .mark{width:7px;height:7px;margin-right:3px}
.notepad .contact{position:absolute;right:14px;top:22px;font-size:3px;line-height:4.4px;color:var(--grey)}
.notepad .lines{position:absolute;left:14px;right:16px;top:65px}
.notepad .lines span{display:block;height:10.3px;border-bottom:1px solid var(--rule)}

/* letterhead */
.letterhead{left:333px;top:192px;width:371px;height:524px}
.letterhead .brand{position:absolute;left:29px;top:43px;font-size:12.5px}
.letterhead .mark{width:13px;height:13px;margin-right:4px}
.contact-block{position:absolute;left:265px;top:29px;font-size:5.2px;line-height:7.6px;color:var(--grey)}
.contact-block i{display:inline-block;width:4px;height:4px;border-radius:50%;background:var(--red);margin-right:3px;vertical-align:middle}
.letter{position:absolute;left:29px;top:138px;width:308px;font-size:4.6px;line-height:7.3px;color:#555}
.letter .salutation{font-size:8.5px;color:var(--ink);margin-bottom:15px}
.letter p{margin-bottom:7.5px;text-align:justify}
.signature{width:104px;height:36px;margin-top:6px;background:linear-gradient(90deg,rgba(60,60,60,.18),rgba(60,60,60,.05))}

/* folder */
.folder{left:728px;top:194px;width:404px;height:551px;background:var(--red)}
.folder .spine{position:absolute;left:348px;top:0;bottom:0;width:1.5px;background:rgba(255,255,255,.75)}
.folder .brand{position:absolute;left:82px;top:246px;font-size:30px;letter-spacing:.17em}
.folder .mark{width:30px;height:30px;margin-right:9px}

/* business cards */
.card{width:159px;height:90px;left:122px}
.card-front{top:508px}
.card-front .brand{position:absolute;right:10px;top:9px;font-size:8.5px}
.card-front .mark{width:8px;height:8px;margin-right:3px}
.card-front .name{position:absolute;left:10px;top:51px;font-size:5px;font-weight:600;color:var(--red)}
.card-front .role{position:absolute;left:10px;top:57px;font-size:3.6px;color:var(--grey)}
.card-front .divider{position:absolute;left:10px;right:10px;top:63px;height:.8px;background:linear-gradient(90deg,var(--red) 0 50%,var(--rule) 50%)}
.card-front .details{position:absolute;left:10px;top:68px;font-size:3.2px;line-height:4.3px;color:var(--grey)}
.card-front .address{position:absolute;right:10px;top:72px;font-size:3.2px;line-height:4.3px;color:var(--grey);text-align:right}
.card-back{top:627px;background:var(--red-deep)}
.card-back .brand{position:absolute;left:30px;top:38px;font-size:13px}
.card-back .mark{width:12px;height:12px;margin-right:4px}

/* envelopes */
.envelope-front{left:188px;top:806px;width:387px;height:192px}
.envelope-front .brand{position:absolute;left:17px;top:14px;font-size:10px}
.envelope-front .mark{width:10px;height:10px;margin-right:3px}
.envelope-front .address{position:absolute;left:17px;top:28px;font-size:4.6px;line-height:6.4px;color:var(--grey)}
.envelope-back{left:314px;top:749px;width:388px;height:193px}
.envelope-back .flap{position:absolute;left:0;right:0;top:0;height:54px;background:var(--red);border-radius:0 0 6px 6px}
.envelope-back .flap .mark{position:absolute;left:181px;top:13px;width:21px;height:21px;background:#fff}
.envelope-back .flap .web{position:absolute;left:0;right:0;top:39px;text-align:center;font-size:3.4px;letter-spacing:.2em;color:#fff}

/* pens */
.pen{position:absolute;left:720px;width:240px;height:10px}
.pen .barrel{position:absolute;left:8px;right:14px;top:0;height:9px;border-radius:2px 4px 4px 2px;background:#fafafa;box-shadow:0 1px 2px rgba(0,0,0,.15)}
.pen .tip{position:absolute;left:0;top:2.5px;width:12px;height:4px;border-radius:3px 0 0 3px;background:#e8e8e8}
.pen .cap{position:absolute;right:0;top:1.5px;width:16px;height:6px;border-radius:1px;background:#d9d9d9}
.pen .clip{position:absolute;left:144px;top:8px;width:80px;height:3px;border-radius:2px;background:#cfcfcf}
.pen .ring{position:absolute;left:94px;top:0;width:2px;height:9px;background:#c8c8c8}
.pen .brand{position:absolute;left:170px;top:2px;font-size:5px}
.pen .mark{width:4.5px;height:4.5px;margin-right:1.5px}
.pen--red .barrel{background:var(--red)}
.pen--red .brand{color:#fff}
.pen--red .mark{background:#fff}

/* buttons */
.badge{position:absolute;top:957px;width:44px;height:44px;border-radius:50%;display:flex;align-items:center;justify-content:center;box-shadow:0 1px 3px rgba(0,0,0,.2)}
.badge .brand{font-size:3.6px;letter-spacing:.12em}
.badge .mark{width:3.5px;height:3.5px;margin-right:1px}
.badge--white{left:595px;background:#fafafa}
.badge--red{left:664px;background:var(--red)}
.badge--grey{left:735px;background:var(--grey)}
</style>
</head>
<body>
<div class="canvas">

  <div class="piece banner">
    <div class="brand"><span class="mark"></span>LumaGrin</div>
  </div>

  <div class="piece notepad">
    <div class="rings"><span></span><span></span><span></span><span></span><span></span><span></span><span></span><span></span><span></span><span></span><span></span><span></span></div>
    <div class="brand"><span class="mark"></span>LumaGrin</div>
    <div class="contact">1420 Willow Crest Road<br>Bellmont, Oregon 97321<br>555-204-7318<br>info@lumagrin.com<br>www.lumagrin.com</div>
    <div class="lines"><span></span><span></span><span></span><span></span><span></span><span></span><span></span><span></span><span></span><span></span><span></span><span></span><span></span><span></span><span></span><span></span></div>
    <div class="edge-band"></div>
  </div>

  <div class="piece letterhead">
    <div class="brand"><span class="mark"></span>LumaGrin</div>
    <div class="contact-block">1420 Willow Crest Road<br>Bellmont, Oregon 97321<br><i></i>555-204-7318<br><i></i>info@lumagrin.com<br><i></i>www.lumagrin.com</div>
    <div class="letter">
      <div class="salutation">Dear Mr. Hale,</div>
      <p>Thank you for choosing our clinic for your family's dental care. We are pleased to confirm your first visit and to share a short overview of the treatments, opening hours and services offered at our new practice this summer.</p>
      <p>Our team brings years of experience in general, cosmetic and preventive dentistry. Every room is fitted with modern equipment so that each check-up, cleaning and treatment is calm, precise and comfortable from start to finish.</p>
      <p>Please arrive ten minutes early so we can complete your records. Bring a list of any medicines you take and your insurance card. If you need to change the time, simply call our front desk or send us an email.</p>
      <p>We also offer whitening, aligners and gentle care for children, with flexible payment plans for every treatment. Our staff will gladly explain each option during your visit and help you choose what suits you best.</p>
      <p>We look forward to welcoming you and your family to the clinic very soon.</p>
      <p style="margin-top:12px">Sincerely,</p>
      <div class="signature" role="img" aria-label="Handwritten signature"></div>
    </div>
    <div class="edge-band" style="height:4px"></div>
  </div>

  <div class="piece folder">
    <div class="spine"></div>
    <div class="brand brand--light"><span class="mark"></span>LumaGrin</div>
  </div>

  <div class="piece card card-front">
    <div class="brand"><span class="mark"></span>LumaGrin</div>
    <div class="name">DANIEL HALE</div>
    <div class="role">President</div>
    <div class="divider"></div>
    <div class="details">555-204-7318<br>info@lumagrin.com<br>www.lumagrin.com</div>
    <div class="address">1420 Willow Crest Road<br>Bellmont, Oregon 97321</div>
    <div class="edge-band" style="height:2px"></div>
  </div>

  <div class="piece card card-back">
    <div class="brand brand--light"><span class="mark"></span>LumaGrin</div>
  </div>

  <div class="piece envelope-front">
    <div class="brand"><span class="mark"></span>LumaGrin</div>
    <div class="address">1420 Willow Crest Road<br>Bellmont, Oregon 97321</div>
    <div class="edge-band" style="height:2.5px"></div>
  </div>

  <div class="piece envelope-back">
    <div class="flap">
      <span class="mark"></span>
      <div class="web">www.LumaGrin.com</div>
    </div>
  </div>

  <div class="pen" style="top:808px">
    <div class="tip"></div><div class="barrel"></div><div class="ring"></div><div class="cap"></div><div class="clip"></div>
    <div class="brand"><span class="mark"></span>LumaGrin</div>
  </div>
  <div class="pen pen--red" style="top:848px">
    <div class="tip"></div><div class="barrel"></div><div class="ring"></div><div class="cap"></div><div class="clip"></div>
    <div class="brand"><span class="mark"></span>LumaGrin</div>
  </div>
  <div class="pen" style="top:889px">
    <div class="tip"></div><div class="barrel"></div><div class="ring"></div><div class="cap"></div><div class="clip"></div>
    <div class="brand"><span class="mark"></span>LumaGrin</div>
  </div>

  <div class="badge badge--white"><div class="brand"><span class="mark"></span>LumaGrin</div></div>
  <div class="badge badge--red"><div class="brand brand--light"><span class="mark"></span>LumaGrin</div></div>
  <div class="badge badge--grey"><div class="brand brand--light"><span class="mark"></span>LumaGrin</div></div>

</div>
</body>
</html>
```